Creative Photography Business Card

Looking for a unique, creative, elegant, sophisticated and professional business card for my photography business.

I specialise in children, families, modelling, weddings and special event photography

Things to include:
Logo - will attach
Email: hello@mirabellwoodsphoto.com.au
web:www.mirabellwoodsphoto.com.au
Ph: 0438 502 671

I will also upload some of my work that you may like to use.

Please be creative and unique in your designs.

```html
<!DOCTYPE html>
<html lang="en">
<head>
<meta charset="utf-8">
<title>Mirabell Woods Photography – Business Card</title>
<link rel="stylesheet" href="https://fonts.googleapis.com/css2?family=Lato:wght@400;700&display=swap">
<style>
  :root {
    --page-bg: #e9eaec;
    --brand-blue: #20609d;
    --card-white: #ffffff;
    --text-white: #ffffff;
    --divider: rgba(255, 255, 255, 0.85);
    --card-shadow: rgba(20, 30, 45, 0.2);
  }
  * { margin: 0; padding: 0; box-sizing: border-box; }
  html, body {
    width: 1200px;
    height: 926px;
    overflow: hidden;
    background: var(--page-bg);
    font-family: "Lato", sans-serif;
  }
  .canvas { position: relative; width: 1200px; height: 926px; }
  .card {
    position: absolute;
    left: 280px;
    width: 640px;
    height: 391px;
    overflow: hidden;
    box-shadow: 0 6px 18px var(--card-shadow);
  }
  .card--front { top: 52px; background: var(--card-white); }
  .card--back { top: 483px; }

  /* Front side */
  .front__brand {
    position: absolute;
    top: 0; left: 0;
    width: 100%;
    height: 150px;
    display: flex;
    align-items: center;
    justify-content: center;
    gap: 12px;
  }
  .brand-mark {
    width: 14px;
    height: 14px;
    border-radius: 50%;
    background: var(--brand-blue);
  }
  .brand-name {
    font-weight: 400;
    font-size: 24px;
    letter-spacing: 1px;
    color: var(--brand-blue);
  }
  .front__band {
    position: absolute;
    left: 0; bottom: 0;
    width: 100%;
    height: 241px;
    background: var(--brand-blue);
    padding-top: 46px;
  }
  .contact-list { list-style: none; text-align: center; }
  .contact-item {
    color: var(--text-white);
    font-size: 19px;
    line-height: 1.55;
    letter-spacing: 0.8px;
  }
  .contact-label { font-weight: 700; }

  /* Back side */
  .collage { display: block; width: 640px; height: 391px; }
  .back__brand {
    position: absolute;
    left: 14px;
    bottom: 40px;
    width: 180px;
    text-align: center;
    font-weight: 400;
    font-size: 17px;
    line-height: 1.25;
    color: var(--text-white);
    letter-spacing: 0.5px;
  }
</style>
</head>
<body>
<main class="canvas">

  <section class="card card--front" aria-label="Business card front">
    <div class="front__brand">
      <span class="brand-mark" aria-hidden="true"></span>
      <span class="brand-name">Mirabell Woods Photography</span>
    </div>
    <div class="front__band">
      <ul class="contact-list">
        <li class="contact-item"><span class="contact-label">phone:</span> 0438 502 671</li>
        <li class="contact-item"><span class="contact-label">web:</span> mirabellwoodsphoto.com.au</li>
        <li class="contact-item"><span class="contact-label">email:</span> hello@mirabellwoodsphoto.com.au</li>
      </ul>
    </div>
  </section>

  <section class="card card--back" aria-label="Business card back">
    <svg class="collage" viewBox="0 0 640 391" xmlns="http://www.w3.org/2000/svg">
      <defs>
        <linearGradient id="toneWedding" x1="0" y1="0" x2="0.6" y2="1">
          <stop offset="0" stop-color="#f3dfb8"/>
          <stop offset="0.3" stop-color="#b98d6c"/>
          <stop offset="0.6" stop-color="#3b2c28"/>
          <stop offset="1" stop-color="#7d9b4c"/>
        </linearGradient>
        <radialGradient id="glowWedding" cx="0.4" cy="0.55" r="0.35">
          <stop offset="0" stop-color="#e7b99a" stop-opacity="0.9"/>
          <stop offset="1" stop-color="#e7b99a" stop-opacity="0"/>
        </radialGradient>
        <linearGradient id="toneFamily" x1="0" y1="0" x2="0.5" y2="1">
          <stop offset="0" stop-color="#5d8a3c"/>
          <stop offset="0.35" stop-color="#9ab7c9"/>
          <stop offset="0.65" stop-color="#34414f"/>
          <stop offset="1" stop-color="#8f7a5e"/>
        </linearGradient>
        <radialGradient id="glowFamily" cx="0.55" cy="0.5" r="0.35">
          <stop offset="0" stop-color="#d8a487" stop-opacity="0.8"/>
          <stop offset="1" stop-color="#d8a487" stop-opacity="0"/>
        </radialGradient>
        <linearGradient id="toneTeen" x1="0" y1="0" x2="0.4" y2="1">
          <stop offset="0" stop-color="#c9c3b6"/>
          <stop offset="0.35" stop-color="#5a3422"/>
          <stop offset="0.7" stop-color="#d8b49a"/>
          <stop offset="1" stop-color="#efe6da"/>
        </linearGradient>
        <radialGradient id="glowTeen" cx="0.55" cy="0.42" r="0.3">
          <stop offset="0" stop-color="#e3b394" stop-opacity="0.95"/>
          <stop offset="1" stop-color="#e3b394" stop-opacity="0"/>
        </radialGradient>
        <linearGradient id="toneChildren" x1="0" y1="0" x2="0.3" y2="1">
          <stop offset="0" stop-color="#cfc9be"/>
          <stop offset="0.3" stop-color="#2f3b57"/>
          <stop offset="0.55" stop-color="#a46c4c"/>
          <stop offset="1" stop-color="#f08a3e"/>
        </linearGradient>
        <radialGradient id="glowChildren" cx="0.5" cy="0.45" r="0.4">
          <stop offset="0" stop-color="#c08563" stop-opacity="0.95"/>
          <stop offset="1" stop-color="#c08563" stop-opacity="0"/>
        </radialGradient>
        <radialGradient id="glowChildrenSmall" cx="0.82" cy="0.85" r="0.25">
          <stop offset="0" stop-color="#f1c2a5" stop-opacity="0.9"/>
          <stop offset="1" stop-color="#f1c2a5" stop-opacity="0"/>
        </radialGradient>
      </defs>

      <g role="img" aria-label="Photo of a toddler and a wedding couple">
        <polygon points="0,0 160,0 -100,391 0,391" fill="url(#toneWedding)"/>
        <polygon points="0,0 160,0 -100,391 0,391" fill="url(#glowWedding)"/>
      </g>
      <g role="img" aria-label="Photo of a family group outdoors">
        <polygon points="160,0 340,0 80,391 -100,391" fill="url(#toneFamily)"/>
        <polygon points="160,0 340,0 80,391 -100,391" fill="url(#glowFamily)"/>
      </g>
      <g role="img" aria-label="Portrait of a teenage girl resting her chin on her hands">
        <polygon points="340,0 470,0 210,391 80,391" fill="url(#toneTeen)"/>
        <polygon points="340,0 470,0 210,391 80,391" fill="url(#glowTeen)"/>
      </g>
      <g role="img" aria-label="Photo of two smiling children">
        <polygon points="470,0 640,0 640,391 210,391" fill="url(#toneChildren)"/>
        <polygon points="470,0 640,0 640,391 210,391" fill="url(#glowChildren)"/>
        <polygon points="470,0 640,0 640,391 210,391" fill="url(#glowChildrenSmall)"/>
      </g>

      <g class="strip-dividers" stroke="var(--divider)" stroke-width="2">
        <line x1="160" y1="0" x2="-100" y2="391"/>
        <line x1="340" y1="0" x2="80" y2="391"/>
        <line x1="470" y1="0" x2="210" y2="391"/>
      </g>

      <polygon class="brand-panel" points="0,300 190,232 245,391 0,391" fill="var(--brand-blue)"/>
    </svg>
    <div class="back__brand">Mirabell Woods Photography</div>
  </section>

</main>
</body>
</html>
```